Flyer for The Quiet Bloom Gathering

I am launching my new offering in my business at an event next Sunday where I have a booth and need a flyer advertising the offering, so the flyer needs to stand out for other practitioners that will also be there on the day offering there services.
This flyer is also what I will use for marketing on social media as well as on the day of the event. See the link below to the offering
http://sarahlindqvist.com.au/quiet-bloom-gathering/

Target Market(s)

Women with body image issues - age range 25 - 65
Women with issues around food such as binge eating, emotional eating, eating disorders.

Industry/Entity Type

Health And Wellness

Font styles to use
Serif
Sans Serif
Script

Colors
f9d9e8
85cae6
cee9f5
fee18a
ffffff
eea4c8

Requirements
Must have
• Colours matching my overall website at sarahlindqvist.com.au - pinks, light blue, gold, white
• Imagery similiar to my Instagram, see below https://www.instagram.com/riverstonecarexy/
• - soft, warm, welcoming, nurturing, safe, inviting - see image on sales page for inspiration
• contact details
Should not have
• harsh dark colours or harsh lines

```html
<!DOCTYPE html>
<html lang="en">
<head>
<meta charset="utf-8">
<title>The Quiet Bloom Gathering – Flyer</title>
<link rel="stylesheet" href="https://fonts.googleapis.com/css2?family=Oswald:wght@500;600;700&family=Poppins:wght@400;500;600&family=Lobster&family=Libre+Baskerville:ital@1&display=swap">
<style>
  :root {
    --pink: #ec4f8b;
    --pink-soft: #f9d9e8;
    --teal: #1fb8d0;
    --teal-light: #a9e5ef;
    --ink: #1f1f1f;
    --white: #ffffff;
    --gold: #e8b64a;
  }
  * { margin: 0; padding: 0; box-sizing: border-box; }
  html, body { width: 1041px; height: 1200px; overflow: hidden; background: var(--white); }
  .flyer { position: relative; width: 1041px; height: 1200px; overflow: hidden; font-family: "Poppins", Arial, sans-serif; color: var(--ink); }
  .flyer-shapes { position: absolute; inset: 0; }

  .brand { position: absolute; top: 36px; left: 235px; width: 440px; text-align: center; }
  .brand-name { font-family: "Poppins", sans-serif; font-weight: 500; font-size: 40px; color: var(--pink); letter-spacing: 1px; line-height: 1; }
  .brand-tagline { margin-top: 8px; font-size: 10.5px; font-weight: 600; color: var(--teal); white-space: nowrap; }
  .brand-tagline::before { content: ""; display: block; width: 300px; height: 2px; margin: 0 auto 5px; background: linear-gradient(90deg, var(--pink), var(--gold), var(--teal)); }

  .title { position: absolute; top: 124px; left: 290px; width: 350px; text-align: center; font-family: "Oswald", sans-serif; font-weight: 600; line-height: 0.95; text-transform: uppercase; letter-spacing: -1px; }
  .title-line-1 { display: block; font-size: 80px; color: var(--pink); }
  .title-line-2 { display: block; font-size: 56px; color: var(--teal); }
  .title-line-3 { display: block; font-size: 80px; color: var(--pink); }

  .portrait { position: absolute; left: 80px; top: 492px; width: 206px; height: 206px; border-radius: 50%; border: 4px solid var(--white); background: radial-gradient(circle at 50% 40%, #f3d7c8, #e7b7a6 55%, #d69aa6); box-shadow: 0 2px 8px rgba(0,0,0,0.15); }

  .left-pitch { position: absolute; left: 28px; top: 712px; width: 310px; text-align: center; font-size: 18.5px; line-height: 26px; color: var(--ink); }
  .ready { position: absolute; left: 26px; top: 996px; width: 320px; text-align: center; font-family: "Lobster", cursive; font-size: 33px; line-height: 40px; color: var(--pink); }
  .call-label { position: absolute; left: 30px; top: 1050px; font-family: "Oswald", sans-serif; font-weight: 600; font-size: 24px; line-height: 30px; color: var(--ink); }
  .call-number { position: absolute; left: 30px; top: 1080px; font-family: "Oswald", sans-serif; font-weight: 700; font-size: 42px; line-height: 52px; color: var(--ink); letter-spacing: 0.5px; }
  .contact-list { position: absolute; left: 24px; top: 1144px; list-style: none; font-size: 14px; font-weight: 600; color: var(--ink); }
  .contact-list li { display: flex; align-items: center; gap: 8px; height: 22px; }
  .contact-list svg { width: 15px; height: 15px; }

  .intro { position: absolute; left: 370px; top: 520px; width: 662px; text-align: center; font-family: "Libre Baskerville", Georgia, serif; font-style: italic; font-size: 12.6px; line-height: 20.8px; color: var(--ink); }
  .band { position: absolute; left: 362px; width: 679px; background: var(--pink); color: var(--white); font-weight: 400; font-size: 20px; line-height: 27px; padding: 2px 20px; }
  .band-commit { top: 736px; height: 31px; }
  .band-receive { top: 938px; height: 74px; padding: 10px 22px; }
  .body-copy { position: absolute; left: 392px; top: 787px; width: 620px; text-align: center; font-size: 15.5px; line-height: 21.5px; }
  .body-copy p + p { margin-top: 14px; }
  .body-copy em { font-style: italic; }
  .benefits { position: absolute; left: 386px; top: 1030px; width: 640px; list-style: none; font-size: 15.5px; line-height: 21.5px; }
  .benefits li { position: relative; padding-left: 26px; margin-bottom: 8px; }
  .benefits li::before { content: ""; position: absolute; left: 4px; top: 8px; width: 6px; height: 6px; border-radius: 50%; background: var(--pink); }
</style>
</head>
<body>
<main class="flyer">
  <svg class="flyer-shapes" width="1041" height="1200" viewBox="0 0 1041 1200">
    <defs>
      <linearGradient id="right-wash" x1="0" y1="0" x2="0" y2="1">
        <stop offset="0" stop-color="#ffffff"/>
        <stop offset="1" stop-color="#f9e6ef"/>
      </linearGradient>
      <linearGradient id="left-column" x1="0" y1="0" x2="1" y2="0">
        <stop offset="0" stop-color="#1fb8d0"/>
        <stop offset="1" stop-color="#a9e5ef"/>
      </linearGradient>
      <linearGradient id="band-teal" x1="0" y1="0" x2="1" y2="1">
        <stop offset="0" stop-color="#1fb8d0"/>
        <stop offset="1" stop-color="#5fd0e2"/>
      </linearGradient>
      <linearGradient id="hero-sky" x1="0" y1="0" x2="0" y2="1">
        <stop offset="0" stop-color="#ffffff"/>
        <stop offset="0.35" stop-color="#fbeef0"/>
        <stop offset="0.55" stop-color="#f6d3c6"/>
        <stop offset="0.72" stop-color="#cfdbe6"/>
        <stop offset="1" stop-color="#9fb8c8"/>
      </linearGradient>
    </defs>
    <rect class="right-background" x="0" y="0" width="1041" height="1200" fill="url(#right-wash)"/>
    <rect class="left-column" x="0" y="0" width="362" height="1200" fill="url(#left-column)"/>
    <path class="swoosh-pink" d="M0,0 H1041 V392 C880,478 720,516 560,514 C330,508 90,440 0,380 Z" fill="var(--pink)"/>
    <path class="swoosh-teal" d="M63,0 H1041 V398 C880,476 720,508 560,506 C340,498 110,380 63,0 Z" fill="url(#band-teal)"/>
    <path class="hero-photo" role="img" aria-label="Photo of a woman stretching her arms up towards a soft pastel sunset over the sea"
          d="M151,0 H1041 V386 C880,464 720,496 560,494 C370,486 170,340 151,0 Z" fill="url(#hero-sky)"/>
  </svg>

  <header class="brand">
    <div class="brand-name">Sarah Lindqvist</div>
    <div class="brand-tagline">Find Your Way Back to Peace With Your Body and Your Plate</div>
  </header>

  <h1 class="title">
    <span class="title-line-1">The Quiet</span>
    <span class="title-line-2">Bloom</span>
    <span class="title-line-3">Gathering</span>
  </h1>

  <div class="portrait" role="img" aria-label="Portrait of the host relaxing on a sofa with her small dog"></div>

  <p class="left-pitch">It's time to show up for<br>YOU, consistently, every<br>week, and do the work,<br>once and for all.<br>No more games, no more<br>half in on YOU....<br>You deserve better than a<br>life contained in the<br>mental prison of body<br>hatred.</p>

  <p class="ready">Are you ready?</p>
  <p class="call-label">Call Now</p>
  <p class="call-number">0400 555 172</p>
  <ul class="contact-list">
    <li>
      <svg viewBox="0 0 16 16"><circle cx="8" cy="8" r="7.5" fill="#333"/><rect x="4" y="5.2" width="8" height="5.6" rx="0.6" fill="none" stroke="#fff" stroke-width="1"/><path d="M4.2,5.6 L8,8.4 L11.8,5.6" fill="none" stroke="#fff" stroke-width="1"/></svg>
      sarah@sarahlindqvist.com.au
    </li>
    <li>
      <svg viewBox="0 0 16 16"><circle cx="8" cy="8" r="7.5" fill="#333"/><circle cx="8" cy="8" r="4" fill="none" stroke="#fff" stroke-width="1"/><path d="M4,8 H12 M8,4 V12" stroke="#fff" stroke-width="0.9"/></svg>
      sarahlindqvist.com.au
    </li>
  </ul>

  <p class="intro">
    It's time to make a commitment….<br>
    It's time for YOU, to SHOW UP for YOU…..<br>
    It's time to truly let go…….and finally heal, and find the peace that you so long for…<br>
    You deserve to feel the freedom that comes with truly loving and accepting your body.<br>
    You deserve the freedom that comes with experiencing a deeper trusting<br>
    connection with your body, where you feel safe, at home.<br>
    Can you even imagine a whole day that you didn't hate your body,<br>
    you didn't fight with food, and you felt peaceful and at home with your body?<br>
    Can you love the part of you, that hates your body?<br>
    You can't heal something you hate.
  </p>

  <h2 class="band band-commit">Are you truly ready to make the commitment?</h2>

  <div class="body-copy">
    <p>How would it feel to be able to say, <em>“I am free to love and accept my body”,</em> and <em>“I am free, connected and at peace to my body”</em>?</p>
    <p>I am inviting 10 women only into this six-week healing experience, as I personally know, that when we share our stories, it opens our hearts for other people to share their stories. It gives us the sense we are not alone in our journey's.</p>
  </div>

  <h2 class="band band-receive">The women that come on this six-week<br>journey will receive;</h2>

  <ul class="benefits">
    <li>One 90mins one on one coaching session with me (which for the women that have attended the Friday circle previously, can be done before this healing circle begins);</li>
    <li>Private online group to continue support outside of the circle</li>
    <li>Homework outside of circle to support your healing</li>
    <li>Journal and other small gifts weekly</li>
  </ul>
</main>
</body>
</html>
```